Audio transcription specialist looking for pretty business card design

> Who I am, what I do: Editor, auto entrepreneur, I write meeting minutes for companies (EC, CHSCT, etc.) and transcribe in writing various types of oral interventions (symposia, conferences, interviews, etc.)> My mindset: I would like a business card that stays in the spirit of my website: http://www.plume-minuscule.net/ I would like the final design to be a little whimsical, original, while remaining serious and reflects the independence of my activity. > A few words about my activity: I am in a sector largely dominated by big companies with a rather too serious design (corporate), not so original, even if in evolution. Obviously (like everyone else), I would like to mark my difference! The main advantage for my client is that I take charge of the entire process of document production (no outsourcing, no division of tasks) and that I have at heart to familiarize myself with the culture of his company and his specific problems. > Atmosphere:. I would like the design of the card has an obvious link with my job (it is writing, transcription) without being too cliché. . A modern appearance, freshness. That it reflects my personality: softness, elegance, simplicity, seriousness I tried to create a model of card by taking again the elements of my site (the image on pink background with the helmet, the keyboard, the notebook, etc. ) but it's a little redundant ... I would like something that stays in harmony with this atmosphere: a feminine universe, cozy (see also the image at the bottom of the page, which for once tends a little too much towards the relaxed, but that seems to me welcome to this place because it is about inviting prospects to contact me to discuss their needs). In harmony with what emerges from my site, while being different so that the person who goes to my site after receiving my card does not find the same thing! > Colors: colorful without being too flashy. I give free rein to your imagination for the choice of colors, gray and pink is a possibility, but I'm not at all stopped on it! In any case, no garish colors or raw primary colors. I like for example the magenta of my word cloud because it punctuates a more sober set. > Fonts: I do not know if the use of the font of my site is judicious on a business card (playfair display). Perhaps it could be used for a key element, such as the little sentence describing my services: "audio file to written text", accompanied by another font without impasto, more sober. > Cloud words: ensure that small words remain legible;) If necessary, I can change the proportions on your board.

Target Market(s)

Conference Organizers - Conferences Works Council - Board of Directors Professionals needing to transcribe interviews: Lawyers, sociologists, etc.

Industry/Entity Type

Audio

Contact Information for Business Card

Maëlle Dorsannes
Rédactrice - Spécialiste de la transcription
Du fichier audio au texte écrit
Paris 11e
Tél. 06 41 27 93 58
mail : contact@plume-minuscule.net
adresse du site web : www.plume-minuscule.net

Font styles to use
Sans Serif
Other font styles liked:
• Playfair Display

Colors

Designer to choose colors to be used in the design.

Requirements
Must have
• - Atmosphere:> I would like the design of the card has an obvious link with my job (it is about writing, transcription) without being too cliché. > A modern look, freshness> That it reflects my personality: softness, elegance, simplicity, seriousness
Nice to have
• - Some key words to stimulate the imagination: - freelance writer - liberal profession - quality work - softness - elegance - listening, attention, home - fantasy - cozy - freshness
Should not have
• The garish colors, raw primary colors.

```html
<!DOCTYPE html>
<html lang="fr">
<head>
<meta charset="utf-8">
<title>Plume Minuscule — carte de visite</title>
<link rel="stylesheet" href="https://fonts.googleapis.com/css2?family=Playfair+Display:wght@700;900&family=Roboto:wght@400;500&family=Russo+One&display=swap">
<style>
  :root {
    --page: #e9e6e3;
    --paper: #ffffff;
    --paper-shade: #ededed;
    --ink-dark: #1c1c1e;
    --ink-mid: #3a3a3d;
    --magenta: #e0169a;
    --magenta-deep: #b90d7d;
    --soft-text: #c9c9cc;
    --ghost: rgba(255,255,255,0.07);
  }
  * { box-sizing: border-box; margin: 0; padding: 0; }
  html, body { width: 740px; height: 1200px; overflow: hidden; background: var(--page); }
  .sheet { position: relative; width: 740px; height: 1200px; }

  .card {
    position: absolute; left: 60px; width: 620px; height: 354px;
    border-radius: 16px; overflow: hidden;
    box-shadow: 0 10px 30px rgba(0,0,0,0.18);
  }
  .card--front { top: 150px; background: linear-gradient(180deg, var(--ink-mid), var(--ink-dark)); }
  .card--back  { top: 700px; background: linear-gradient(160deg, #4a4a4e 0%, var(--ink-dark) 60%, #111113 100%); }

  /* front */
  .front__paper {
    position: absolute; left: 0; top: 0; width: 100%; height: 168px;
    background: linear-gradient(180deg, var(--paper), var(--paper-shade));
  }
  .brand {
    position: absolute; left: 0; top: 0; width: 100%; height: 168px;
    display: flex; align-items: center; justify-content: center; gap: 12px;
  }
  .brand__dot { width: 12px; height: 12px; border-radius: 50%; background: var(--magenta); }
  .brand__name {
    font-family: "Playfair Display", Georgia, serif; font-weight: 900;
    font-size: 38px; color: var(--magenta); letter-spacing: 0.5px;
  }
  .band { position: absolute; left: 0; top: 168px; width: 620px; height: 40px; }
  .band__address {
    position: absolute; left: 22px; top: 168px; height: 40px;
    display: flex; align-items: center; gap: 8px;
    font-family: "Roboto", Arial, sans-serif; font-size: 15px; color: #fff;
  }
  .contacts {
    position: absolute; left: 26px; top: 240px; list-style: none;
    font-family: "Roboto", Arial, sans-serif; font-size: 14px; color: var(--soft-text);
  }
  .contacts li { display: flex; align-items: center; gap: 10px; height: 26px; }
  .contacts svg { flex: none; }
  .identity { position: absolute; right: 30px; top: 236px; text-align: right; }
  .identity__name {
    font-family: "Russo One", Arial, sans-serif; font-size: 22px;
    color: var(--magenta); letter-spacing: 1px; text-transform: uppercase;
  }
  .identity__role {
    font-family: "Roboto", Arial, sans-serif; font-size: 14px; color: var(--soft-text); margin-top: 4px;
  }

  /* back */
  .ghost-mark {
    position: absolute; left: 0; top: 0; width: 100%; height: 100%;
    display: flex; align-items: center; justify-content: center;
    font-family: "Playfair Display", Georgia, serif; font-weight: 900;
    font-size: 74px; color: var(--ghost); white-space: nowrap;
  }
  .back__url {
    position: absolute; left: 0; top: 0; width: 100%; height: 100%;
    display: flex; align-items: center; justify-content: center;
    font-family: "Roboto", Arial, sans-serif; font-size: 26px; color: #fff; letter-spacing: 0.3px;
  }
  .back__stripe { position: absolute; left: 0; bottom: 0; width: 100%; height: 8px; background: var(--magenta); }
</style>
</head>
<body>
<main class="sheet">

  <section class="card card--front" aria-label="Recto de la carte">
    <div class="front__paper"></div>
    <div class="brand">
      <span class="brand__dot"></span>
      <span class="brand__name">plume minuscule</span>
    </div>

    <svg class="band" viewBox="0 0 620 40" aria-hidden="true">
      <polygon points="0,0 560,0 580,20 560,40 0,40" fill="var(--magenta)"/>
      <polygon points="560,0 580,20 560,40 620,40 620,0" fill="var(--magenta-deep)" opacity="0.0"/>
      <polygon points="0,40 560,40 556,44 0,44" fill="var(--magenta-deep)"/>
    </svg>
    <div class="band__address">
      <svg width="12" height="16" viewBox="0 0 12 16" aria-hidden="true">
        <path d="M6 0C2.7 0 0 2.6 0 5.9 0 10.3 6 16 6 16s6-5.7 6-10.1C12 2.6 9.3 0 6 0zm0 8.2a2.3 2.3 0 1 1 0-4.6 2.3 2.3 0 0 1 0 4.6z" fill="#fff"/>
      </svg>
      <span>Atelier 14, 22 rue des Lilas, 75011 Paris</span>
    </div>

    <ul class="contacts">
      <li>
        <svg width="10" height="12" viewBox="0 0 10 12" aria-hidden="true"><path d="M2 0l2 3-1.2 1.2c.6 1.5 1.6 2.6 3 3.3L7 6.3l3 2L8.6 11C4 10.5.5 6.4 0 1.6z" fill="var(--magenta)"/></svg>
        <span>06 41 27 93 58</span>
      </li>
      <li>
        <svg width="12" height="9" viewBox="0 0 12 9" aria-hidden="true"><rect width="12" height="9" rx="1" fill="var(--magenta)"/><path d="M0 1l6 4 6-4" stroke="var(--ink-dark)" fill="none"/></svg>
        <span>contact@plume-minuscule.net</span>
      </li>
      <li>
        <svg width="11" height="11" viewBox="0 0 11 11" aria-hidden="true"><circle cx="5.5" cy="5.5" r="5" fill="none" stroke="var(--magenta)" stroke-width="1.2"/><path d="M0.5 5.5h10M5.5 0.5c-2 2.6-2 7.4 0 10M5.5 0.5c2 2.6 2 7.4 0 10" stroke="var(--magenta)" fill="none"/></svg>
        <span>www.plume-minuscule.net</span>
      </li>
    </ul>

    <div class="identity">
      <p class="identity__name">Maëlle Dorsannes</p>
      <p class="identity__role">Rédactrice</p>
    </div>
  </section>

  <section class="card card--back" aria-label="Verso de la carte">
    <div class="ghost-mark" aria-hidden="true">plume minuscule</div>
    <p class="back__url">www.plume-minuscule.net</p>
  </section>

</main>
</body>
</html>
```